Holiday Sale 2026 Graphics for New Year

I want to create 10 social media graphics (new Instagram size 4:5 (1080 x 1350 pixels) focusing on our Holiday Sale Graphics, using any of the pics attached. Use the attached pics, NO RANDOM STOCK PHOTOGRAPHY. For the color scheme of the graphics, they should all be complementary to the product colors in the photos.
You can add any of the photos attached but none are required. You can do some of the graphics in all text. I mainly need BOLD text that says one of the headlines with the pics (10 total):
1. 25% OFF Holiday Sale: New You Starts Now!
2. 25% OFF Everything: New Year, New You
3. 25% OFF Christmas Sale 🎁 Feel Amazing Again!
4. Holiday Treat: 25% OFF Your Favorites
5. 25% OFF All Supplements ✨ New Year Reset!
6. Holiday Magic: 25% OFF Every Supplement
7. 25% OFF to Kickstart Your New Year Goals
8. New Year, New Waistline! 25% OFF Sale
9. Holiday Sale: 25% OFF Everything
10. A Better You Begins With 25% OFF

```html
<!DOCTYPE html>
<html lang="en">
<head>
<meta charset="utf-8">
<title>Holiday Sale Social Graphics</title>
<link href="https://fonts.googleapis.com/css2?family=Oswald:wght@600;700&display=swap" rel="stylesheet">
<style>
:root{
  --board:#8a8a8a;
  --blue:#2b55a5;
  --blue-light:#3f74be;
  --magenta:#b8508f;
  --magenta-light:#d172b1;
  --green:#3f6653;
  --green-panel:#4a6c59;
  --green-light:#6c9a84;
  --charcoal:#2b2a2b;
  --pink:#e57fb2;
  --white:#ffffff;
  --studio-top:#ffffff;
  --studio-bottom:#e2e2e2;
  --marble:#ebe8e3;
}
*{margin:0;padding:0;box-sizing:border-box}
html,body{width:1200px;height:596px;overflow:hidden;background:var(--board)}
.board{position:relative;width:1200px;height:596px;background:var(--board)}
.post{position:absolute;width:226px;height:283px;overflow:hidden;font-family:'Oswald',sans-serif;font-weight:700;text-transform:uppercase}
.post--studio{background:linear-gradient(180deg,var(--studio-top) 0%,var(--studio-bottom) 100%)}
.post--dark{background:var(--charcoal)}
.r1{top:11px}.r2{top:304px}
.c1{left:13px}.c2{left:250px}.c3{left:487px}.c4{left:726px}.c5{left:963px}
.headline{position:absolute;left:0;right:0;line-height:1.08;z-index:2}
.headline--center{text-align:center}
.headline--left{left:17px;right:auto;width:86px;line-height:.98}
.headline span{display:block;white-space:nowrap}
.headline--left span{transform:scaleX(.86);transform-origin:left center;letter-spacing:-.2px}
.blue{color:var(--blue)}.magenta{color:var(--magenta)}.green{color:var(--green)}.pink{color:var(--pink)}.white{color:var(--white)}
.ruled{display:flex!important;align-items:center;justify-content:center;gap:8px}
.ruled::before,.ruled::after{content:"";display:block;width:28px;height:2px;background:currentColor}
.backdrop{position:absolute;inset:0}
.photo{position:absolute;border-radius:4px}
.photo--bottles{background:linear-gradient(180deg,#f2f0ee 0%,#dcd6dd 55%,#c9bfcb 100%)}
.photo--bottles-dark{background:linear-gradient(180deg,#3a3939 0%,#cfcfd2 55%,#e9e6e8 100%)}
.photo--person{background:linear-gradient(180deg,#3b2c26 0%,#2a2222 60%,#e9e6e2 100%);border-radius:60px 60px 4px 4px}
.photo--person-light{background:linear-gradient(180deg,#3b2c26 0%,#e9e2da 45%,#d8d3d6 100%);border-radius:50px 50px 4px 4px}
.photo--bottle-row{background:linear-gradient(180deg,#f4f2f3 0%,#dcd6dd 100%)}
.counter{position:absolute;left:0;right:0;bottom:0;height:33px;background:var(--marble)}
</style>
</head>
<body>
<main class="board">

  <section class="post post--studio r1 c1">
    <h2 class="headline headline--center" style="top:31px">
      <span class="blue" style="font-size:36px">25% Off</span>
      <span class="blue" style="font-size:23px">Holiday Sale:</span>
      <span class="magenta" style="font-size:36px">New You</span>
      <span class="magenta" style="font-size:25px">Starts Now!</span>
    </h2>
    <div class="photo photo--bottles" role="img" aria-label="Four supplement bottles lined up on a white table" style="left:18px;top:168px;width:192px;height:84px"></div>
  </section>

  <section class="post r1 c2">
    <svg class="backdrop" viewBox="0 0 226 283" aria-hidden="true">
      <rect width="226" height="283" fill="var(--green-light)"/>
      <circle cx="-60" cy="60" r="215" fill="var(--green-panel)"/>
    </svg>
    <div class="counter"></div>
    <div class="photo photo--person" role="img" aria-label="Woman in a sheer black top presenting three supplement bottles on a counter" style="left:104px;top:56px;width:116px;height:196px"></div>
    <h2 class="headline headline--left white" style="top:14px">
      <span style="font-size:24px">Holiday</span>
      <span style="font-size:34px">Treat</span>
      <span style="font-size:38px">25%</span>
      <span style="font-size:52px">Off</span>
      <span style="font-size:34px">Your</span>
      <span style="font-size:20px">Favorites</span>
    </h2>
  </section>

  <section class="post post--dark r1 c3">
    <h2 class="headline headline--center" style="top:30px">
      <span class="pink" style="font-size:39px">25% Off</span>
      <span class="pink" style="font-size:25px">To Kickstart</span>
      <span class="white ruled" style="font-size:32px">Your</span>
      <span class="white" style="font-size:23px">New Year Goals</span>
    </h2>
    <div class="photo photo--bottles-dark" role="img" aria-label="Supplement bottles arranged on a stone block against a dark backdrop" style="left:7px;top:170px;width:204px;height:90px"></div>
  </section>

  <section class="post post--studio r1 c4">
    <h2 class="headline headline--center" style="top:25px">
      <span class="green" style="font-size:33px">25% Off</span>
      <span class="green" style="font-size:26px">Everything</span>
      <span class="magenta" style="font-size:33px">New Year</span>
      <span class="magenta" style="font-size:34px">New You</span>
    </h2>
    <div class="photo photo--bottles" role="img" aria-label="Four supplement bottles lined up on a white table" style="left:18px;top:168px;width:192px;height:84px"></div>
  </section>

  <section class="post post--studio r1 c5">
    <h2 class="headline headline--center" style="top:36px">
      <span class="magenta" style="font-size:26px">Holiday Sale</span>
      <span class="blue" style="font-size:39px">25% Off</span>
      <span class="blue" style="font-size:31px">Everything</span>
    </h2>
    <div class="photo photo--bottles" role="img" aria-label="Four supplement bottles grouped closely on a white table" style="left:25px;top:159px;width:163px;height:100px"></div>
  </section>

  <section class="post post--studio r2 c1">
    <h2 class="headline headline--center" style="top:18px">
      <span class="magenta" style="font-size:37px">New Year,</span>
      <span class="magenta" style="font-size:26px">New Waistline!</span>
      <span class="green" style="font-size:43px">25% Off</span>
      <span class="green ruled" style="font-size:29px">Sale</span>
    </h2>
    <div class="photo photo--bottles" role="img" aria-label="Four supplement bottles grouped closely on a white table" style="left:25px;top:162px;width:170px;height:100px"></div>
  </section>

  <section class="post r2 c2">
    <svg class="backdrop" viewBox="0 0 226 283" aria-hidden="true">
      <rect width="226" height="283" fill="var(--magenta-light)"/>
      <circle cx="-60" cy="60" r="215" fill="var(--magenta)"/>
    </svg>
    <div class="counter"></div>
    <div class="photo photo--person" role="img" aria-label="Woman in a sheer black top presenting three supplement bottles on a counter" style="left:106px;top:56px;width:114px;height:196px"></div>
    <h2 class="headline headline--left white" style="top:12px">
      <span style="font-size:24px">A Better</span>
      <span style="font-size:48px">You</span>
      <span style="font-size:30px">Begins</span>
      <span style="font-size:40px">With</span>
      <span style="font-size:38px">25%</span>
      <span style="font-size:52px">Off</span>
    </h2>
  </section>

  <section class="post r2 c3">
    <svg class="backdrop" viewBox="0 0 226 283" aria-hidden="true">
      <rect width="226" height="283" fill="var(--blue-light)"/>
      <circle cx="-40" cy="60" r="230" fill="var(--blue)"/>
    </svg>
    <div class="counter"></div>
    <div class="photo photo--person-light" role="img" aria-label="Smiling woman in a white knit top" style="left:113px;top:85px;width:96px;height:150px"></div>
    <div class="photo photo--bottle-row" role="img" aria-label="Full row of supplement bottles on a counter" style="left:88px;top:220px;width:126px;height:44px"></div>
    <h2 class="headline headline--left white" style="left:18px;top:12px">
      <span style="font-size:28px">Holiday</span>
      <span style="font-size:34px">Magic</span>
      <span style="font-size:42px">25%</span>
      <span style="font-size:56px">Off</span>
      <span style="font-size:35px">Every</span>
      <span style="font-size:18px">Supplement</span>
    </h2>
  </section>

  <section class="post post--studio r2 c4">
    <h2 class="headline headline--center" style="top:18px;line-height:1.02">
      <span class="magenta" style="font-size:35px">25% Off</span>
      <span class="magenta" style="font-size:20px">All Supplements</span>
      <span class="blue" style="font-size:36px">New Year</span>
      <span class="blue" style="font-size:52px">Reset!</span>
    </h2>
    <div class="photo photo--bottles" role="img" aria-label="Four supplement bottles lined up on a white table" style="left:18px;top:167px;width:192px;height:86px"></div>
  </section>

  <section class="post r2 c5">
    <svg class="backdrop" viewBox="0 0 226 283" aria-hidden="true">
      <rect width="226" height="283" fill="var(--blue-light)"/>
      <circle cx="-40" cy="60" r="230" fill="var(--blue)"/>
    </svg>
    <div class="counter"></div>
    <div class="photo photo--person-light" role="img" aria-label="Smiling woman in a white knit top" style="left:114px;top:85px;width:92px;height:150px"></div>
    <div class="photo photo--bottle-row" role="img" aria-label="Full row of supplement bottles on a counter" style="left:88px;top:220px;width:126px;height:44px"></div>
    <h2 class="headline headline--left white" style="left:18px;top:14px">
      <span style="font-size:42px">25%</span>
      <span style="font-size:56px">Off</span>
      <span style="font-size:20px">Christmas</span>
      <span style="font-size:45px">Sale</span>
      <span style="font-size:17px">Feel Amazing</span>
      <span style="font-size:30px">Again!</span>
    </h2>
  </section>

</main>
</body>
</html>
```